UK Based Internet hosting Company wants a vibrant eCommerce site designed.

We have only just had our logo and brand designed by Pixel Forum which went so well that we would like to open up our website design project on here too.

The company is called 'Quay Server Lantern' and we provide a range of website hosting, dedicated server, domain name and email solutions that people will be able to purchase online in neatly packaged options from the outset.

Our logo and brand is bright turquoise, black & white (samples of branding will be attached with this project) but we would like the website to be very vibrant with good use of white space rather than a black website.

We want to appeal to end users so web designers, developers and people who would like to host their website. But we also want to appeal to resellers that would like to resell our hosting packages too.

We want a big push on social media and blogging on the site as we would like our brand to be 100% up with Chatterleaf, Murmel, workLoop, Vidplume and Zorbix+. It would be great to have this integrated into the site with share buttons and rating buttons etc.

We would like to see a homepage initially with a view to providing several page layers down to help our in-house developers hook in our back-end into this front end effectively.

Great customer experience and an easy to navigate journey to the checkout when purchasing the hosting packages is paramount !!

We like how the following sites are set-out and presented:

www.brightmarrow.uk
http://www.tallyfold.co.uk
https://www.qv7.net/web-hosting/

Target Market(s)

We have 3 target markets.

Target market 1 - end users, consumers such as Web Designers, Developers and small businesses.

Target Market 2 - Resellers, small businesses that would like to resell our services.

Target Market 3 - Medium to large businesses that would like more of a bespoke solution.

Industry/Entity Type

Internet

Requirements
Must have
• Colourful, bright, bold, easy to navigate and to purchase packages.
• Plenty of call to actions, social media, ratings.
• Video case studies and testimonials would be nice.

```html
<!DOCTYPE html>
<html lang="en">
<head>
<meta charset="utf-8">
<title>Quay Server Lantern – Web Hosting</title>
<link href="https://fonts.googleapis.com/css2?family=Open+Sans:wght@400;600;700&display=swap" rel="stylesheet">
<style>
  :root {
    --teal: #45b394;
    --teal-dark: #3a9e82;
    --white: #ffffff;
    --ink: #444b4f;
    --grey: #5f6468;
    --hero-dark: #0d0d0f;
    --hero-mid: #1e2a33;
    --hero-blue: #2f7fa6;
  }
  * { box-sizing: border-box; margin: 0; padding: 0; }
  html, body { width: 1200px; height: 609px; overflow: hidden; background: var(--white); }
  body { font-family: "Open Sans", Arial, sans-serif; position: relative; }

  .top-strip { position: absolute; left: 0; top: 0; width: 1200px; height: 6px; background: var(--teal); }

  .site-header { position: absolute; left: 0; top: 0; width: 1200px; height: 68px; }
  .support-tab {
    position: absolute; left: 54px; top: 5px; width: 94px; height: 22px;
    background: var(--teal); color: var(--white); font-size: 14px; font-weight: 600;
    display: flex; align-items: center; justify-content: center; gap: 4px;
  }
  .contact-line {
    position: absolute; left: 169px; top: 8px; font-size: 14px; color: var(--grey);
    display: flex; align-items: center; gap: 6px;
  }
  .contact-line .phone { margin-left: 14px; letter-spacing: 0.5px; }
  .brand {
    position: absolute; left: 527px; top: 10px; display: flex; align-items: center; gap: 8px;
  }
  .brand-dot { width: 48px; height: 48px; border-radius: 50%; background: var(--teal); }
  .brand-name { font-size: 19px; font-weight: 600; color: var(--ink); line-height: 1; width: 110px; }
  .signup-btn {
    position: absolute; left: 1056px; top: 5px; width: 90px; height: 34px;
    background: var(--teal); color: var(--white); font-size: 15px;
    display: flex; align-items: center; justify-content: center; gap: 5px;
  }

  .hero { position: absolute; left: 0; top: 68px; width: 1200px; height: 484px; }
  .hero-visual {
    position: absolute; inset: 0;
    background:
      radial-gradient(ellipse 420px 300px at 640px 60px, rgba(140,150,160,0.35), transparent 70%),
      linear-gradient(90deg, var(--hero-dark) 0%, #151719 38%, var(--hero-mid) 55%, var(--hero-blue) 80%, #1f5877 100%);
  }
  .hero-copy { position: absolute; left: 100px; top: 176px; width: 420px; text-align: center; color: var(--white); }
  .hero-title { font-size: 32px; font-weight: 700; line-height: 1.05; }
  .hero-title .accent { display: block; color: var(--teal); letter-spacing: 0.5px; }
  .hero-sub { font-size: 14.5px; margin-top: 6px; }
  .cta-btn {
    display: inline-flex; align-items: center; justify-content: center;
    margin-top: 30px; width: 204px; height: 43px; background: var(--teal);
    color: var(--white); font-size: 17px; font-weight: 700; word-spacing: 4px;
  }
  .price-note { font-size: 13px; margin-top: 8px; }
  .price-note strong { font-weight: 600; }
  .slide-arrow { position: absolute; top: 250px; width: 40px; height: 40px; }
  .slide-arrow.prev { left: 56px; }
  .slide-arrow.next { left: 1106px; }

  .main-nav { position: absolute; left: 0; top: 552px; width: 1200px; height: 57px; background: var(--teal); }
  .main-nav a {
    position: absolute; top: 18px; color: var(--white); font-size: 18.5px; text-decoration: none;
  }
  .main-nav a.active::before {
    content: ""; position: absolute; left: -12px; top: -18px; width: 82px; height: 3px; background: var(--white);
  }
</style>
</head>
<body>
  <div class="top-strip"></div>

  <header class="site-header">
    <div class="support-tab">
      <svg width="11" height="11" viewBox="0 0 12 12"><circle cx="6" cy="6" r="6" fill="#fff"/><rect x="5.2" y="2.5" width="1.6" height="4.5" fill="#45b394"/><rect x="5.2" y="8" width="1.6" height="1.6" fill="#45b394"/></svg>
      Support
    </div>
    <div class="contact-line">
      <svg width="15" height="11" viewBox="0 0 15 11"><rect width="15" height="11" rx="1" fill="#5f6468"/><path d="M0 1l7.5 5L15 1" stroke="#fff" stroke-width="1.2" fill="none"/></svg>
      <span>Email Us</span>
      <svg class="phone-icon" width="13" height="13" viewBox="0 0 13 13" style="margin-left:12px"><rect width="13" height="13" rx="2" fill="#5f6468"/><path d="M4 3c-.8.6-.6 2 .6 3.6S7.6 9.8 8.6 9.4l1-.8-1.6-1.5-.9.6C6.6 7.5 5.5 6.4 5.3 5.8l.6-.9L4.6 3.2z" fill="#fff"/></svg>
      <span class="phone">01632 960 418</span>
    </div>
    <div class="brand">
      <span class="brand-dot"></span>
      <span class="brand-name">Quay Server Lantern</span>
    </div>
    <a class="signup-btn">
      <svg width="12" height="13" viewBox="0 0 12 13"><circle cx="6" cy="3.5" r="3" fill="#fff"/><path d="M0 13c0-4 2.5-5.5 6-5.5S12 9 12 13z" fill="#fff"/></svg>
      Sign up
    </a>
  </header>

  <section class="hero">
    <div class="hero-visual" role="img" aria-label="Row of glowing blue server towers in a dark data centre"></div>
    <div class="hero-copy">
      <h1 class="hero-title">Your website deserves <span class="accent">GREAT WEB HOSTING</span></h1>
      <p class="hero-sub">The UK’s best web hosting backed by free 24x7 support</p>
      <a class="cta-btn">VIEW OUR PACKAGES</a>
      <p class="price-note">From Only <strong>€ 2.15/mth</strong></p>
    </div>
    <svg class="slide-arrow prev" viewBox="0 0 40 40" aria-label="Previous slide"><circle cx="20" cy="20" r="17" fill="none" stroke="#cfcfcf" stroke-width="4"/><path d="M10 20h20M18 12l-8 8 8 8" stroke="#cfcfcf" stroke-width="4.5" fill="none"/></svg>
    <svg class="slide-arrow next" viewBox="0 0 40 40" aria-label="Next slide"><circle cx="20" cy="20" r="17" fill="none" stroke="#cfcfcf" stroke-width="4"/><path d="M10 20h20M22 12l8 8-8 8" stroke="#cfcfcf" stroke-width="4.5" fill="none"/></svg>
  </section>

  <nav class="main-nav">
    <a class="active" style="left:65px">HOME</a>
    <a style="left:162px">COMPANY</a>
    <a style="left:296px">DOMINE NAMES</a>
    <a style="left:488px">RESELLER HOSTING</a>
    <a style="left:704px">BLOG</a>
    <a style="left:794px">RESOURCES</a>
    <a style="left:942px">KUDOS</a>
    <a style="left:1047px">CONTACT</a>
  </nav>
</body>
</html>
```